Exciting new vermouth brand needs a brilliant label!

We need a label design for an exciting new premium Italian Vermouth brand called Brunavera Vermouth.

Brunavera Vermouth is based on a recipe that has been handed down for four generations and is made in the traditional way in the Piedmonte region of Northern Italy.

Brunavera, which means 'heavenly' in Italian has been designed to elevate classic cocktails such as the Negroni, Americano and Manhattan with a base of Italian wine blended with botanicals such as wormwood, orange peel, rhubarb and cinchona. It has a delicately balanced bittersweet profile with hints of vanilla and citrus.

Its competitors include brands such as Vecchia Torre, Parelli and Danvelo (see the uploaded brief for more examples).

The label is for a 50cl dark bottle (please refer to the uploaded brief) and should be based on maximum dimensions of 70mm (width) x 110mm (height). There is no limit to embellishments such as foil printing, embossing or any other premium finishes. The label does not necessarily need to be rectangular.

Feedback will be given quickly and constructively after submissions to ensure that the process is as fair and useful as possible for everyone.

Target Market(s)

25-45 year old Europeans, 50:50 female:male

Industry/Entity Type

Wine / Spirits / Vermouth

Requirements
Must have
• Fantastic design that is distinct from competitors, a premium feel and great lettering.
Should not have
• Generic images or patterns that do not relate to the brand (Brunavera) or the product

```html
<!DOCTYPE html>
<html lang="en">
<head>
<meta charset="utf-8">
<title>Brunavera Vermouth – Label</title>
<link href="https://fonts.googleapis.com/css2?family=Rye&family=Libre+Baskerville:wght@700&family=Pinyon+Script&display=swap" rel="stylesheet">
<style>
  :root {
    --ink: #4a2c26;
    --cream: #efdbbb;
    --tag: #8a5a4a;
    --origin: #6e4f47;
    --script: #7a5e5a;
    --floral-light: #c9b396;
    --floral-dark: #5a4236;
  }
  html, body {
    margin: 0;
    padding: 0;
    width: 982px;
    height: 1200px;
    overflow: hidden;
    background: var(--floral-light);
  }
  .label {
    position: relative;
    width: 982px;
    height: 1200px;
  }
  .label__floral {
    position: absolute;
    inset: 0;
    background:
      radial-gradient(ellipse at 50% 50%, rgba(201,179,150,0.2) 0%, rgba(90,66,54,0.55) 100%),
      linear-gradient(180deg, #a88e74 0%, #c9b396 50%, #a88e74 100%);
    border: 10px solid var(--floral-dark);
    box-sizing: border-box;
  }
  .label__art {
    position: absolute;
    inset: 0;
    width: 982px;
    height: 1200px;
  }
  .brand {
    font-family: "Rye", "Georgia", serif;
    fill: var(--ink);
  }
  .tagline {
    font-family: "Libre Baskerville", "Times New Roman", serif;
    font-weight: 700;
    fill: var(--tag);
    font-size: 40px;
  }
  .origin {
    font-family: "Libre Baskerville", "Times New Roman", serif;
    font-weight: 700;
    fill: var(--origin);
    font-size: 33px;
  }
  .origin-script {
    font-family: "Pinyon Script", "Brush Script MT", cursive;
    fill: var(--script);
    font-size: 118px;
  }
</style>
</head>
<body>
  <main class="label">
    <div class="label__floral" role="img" aria-label="Engraved sepia floral border with peonies and leaves"></div>
    <svg class="label__art" viewBox="0 0 982 1200" xmlns="http://www.w3.org/2000/svg">
      <defs>
        <path id="shield" d="M491,51 C390,51 280,100 165,140 Q165,265 35,270 L35,930 Q165,935 165,1060 C280,1100 390,1146 491,1146 C592,1146 702,1100 817,1060 Q817,935 947,930 L947,270 Q817,265 817,140 C702,100 592,51 491,51 Z"/>
      </defs>
      <use href="#shield" fill="var(--cream)" stroke="var(--ink)" stroke-width="8"/>
      <use href="#shield" fill="none" stroke="var(--ink)" stroke-width="2.5"
           transform="translate(491 600) scale(0.965 0.972) translate(-491 -600)"/>

      <text class="brand" x="148" y="448" font-size="200" textLength="697" lengthAdjust="spacingAndGlyphs">BRUNAVERA</text>
      <text class="brand" x="139" y="628" font-size="214" textLength="748" lengthAdjust="spacingAndGlyphs">VERMOUTH</text>

      <text class="tagline" x="491" y="723" text-anchor="middle" textLength="567" lengthAdjust="spacingAndGlyphs">ELEVATE YOUR COCKTAILS</text>

      <rect class="divider" x="137" y="772" width="708" height="36" rx="18" fill="#a88e74" opacity="0.75"
            role="img" aria-label="Engraved botanical flourish divider"/>

      <text class="origin" x="488" y="891" text-anchor="middle" textLength="359" lengthAdjust="spacingAndGlyphs">MADE IN PIEDMONT,</text>
      <text class="origin-script" x="481" y="1000" text-anchor="middle">Italy</text>
    </svg>
  </main>
</body>
</html>
```